Copper Lantern LLC Business Card

We need a business card design for a newco in Texas. We are a team of professionals who join start ups as founders and help launch their businesses, which are primarily related to food and beverage and the service side of the industry. We love local and craft and are partners in businesses in the local meat, BBQ and Burger, fine dining, and beverage alcohol businesses. Our specialty is finance and the business side of start ups, including assisting with capital raises as principals, not brokers. We do not currently have any logos or graphics for this entity. Our values include helping people succeed, rooting for the underdog, healthy food, the environment and being good citizens.

Target Market(s)

Everybody but also Angel Investors, CPAs, Bankers, Entrepreneurs

Industry/Entity Type

Business

Contact Information for Business Card

Fields for Business Name, Title, Email Address, Phone Number. Place to add mailing address and web domain later.

Font styles to use
Sans Serif

Colors

Designer to choose colors to be used in the design.

Requirements
Should not have
• Pictures of booze bottles or drinks thought there could be a social scene that does not strictly focus on those. No cows, cowboy hats or ranches. We are not a Wall Street type entity so no huge office buildings or skylines.

```html
<!DOCTYPE html>
<html lang="en">
<head>
<meta charset="utf-8">
<title>Copper Lantern LLC Business Card</title>
<link href="https://fonts.googleapis.com/css2?family=Lato:wght@300;400;700;900&display=swap" rel="stylesheet">
<style>
  :root {
    --backdrop: #9a9a9a;
    --card-light: #ecebe8;
    --card-dark: #262626;
    --ink: #111111;
    --ink-soft: #555555;
    --paper-text: #f2f2f2;
    --paper-muted: #9d9d9d;
  }
  * { margin: 0; padding: 0; box-sizing: border-box; }
  html, body {
    width: 1200px;
    height: 900px;
    overflow: hidden;
    background: var(--backdrop);
    font-family: "Lato", sans-serif;
  }
  .stage {
    position: relative;
    width: 1200px;
    height: 900px;
  }
  .card {
    position: absolute;
    top: 150px;
    width: 340px;
    height: 595px;
    box-shadow: 0 10px 24px rgba(0,0,0,0.25);
  }
  .card--front {
    left: 215px;
    background: var(--card-light);
  }
  .card--back {
    left: 645px;
    background: var(--card-dark);
  }
  .brand {
    position: absolute;
    top: 262px;
    left: 0;
    width: 100%;
    display: flex;
    justify-content: center;
    align-items: center;
    gap: 10px;
  }
  .brand__mark {
    width: 14px;
    height: 14px;
    background: var(--ink);
  }
  .brand__name {
    font-weight: 700;
    font-size: 22px;
    letter-spacing: 1.5px;
    color: var(--ink);
    text-transform: uppercase;
  }
  .web {
    position: absolute;
    bottom: 44px;
    width: 100%;
    text-align: center;
    font-size: 14px;
    letter-spacing: 0.6px;
    color: var(--ink-soft);
  }
  .web strong { font-weight: 700; color: #333; }
  .identity {
    position: absolute;
    top: 34px;
    left: 34px;
  }
  .identity__first {
    font-weight: 300;
    font-size: 18px;
    letter-spacing: 1.5px;
    color: var(--paper-muted);
    line-height: 1.1;
  }
  .identity__last {
    font-weight: 700;
    font-size: 18px;
    letter-spacing: 1.5px;
    color: var(--paper-text);
    line-height: 1.2;
  }
  .identity__title {
    margin-top: 6px;
    font-size: 11px;
    letter-spacing: 1.5px;
    color: var(--paper-muted);
  }
  .identity__rule {
    margin-top: 12px;
    width: 16px;
    height: 2px;
    background: var(--paper-text);
  }
  .accent-line {
    position: absolute;
    top: 262px;
    left: 160px;
  }
  .contact {
    position: absolute;
    right: 30px;
    bottom: 36px;
    text-align: right;
    font-size: 13px;
    letter-spacing: 0.6px;
    line-height: 1.7;
    color: #d8d8d8;
  }
</style>
</head>
<body>
  <main class="stage">
    <section class="card card--front" aria-label="Card front">
      <div class="brand">
        <span class="brand__mark"></span>
        <span class="brand__name">Copper Lantern LLC</span>
      </div>
      <p class="web">www.<strong>copperlantern</strong>.com</p>
    </section>

    <section class="card card--back" aria-label="Card back">
      <div class="identity">
        <p class="identity__first">DANIEL</p>
        <p class="identity__last">MARCHETTI</p>
        <p class="identity__title">DIRECTOR</p>
        <div class="identity__rule"></div>
      </div>
      <svg class="accent-line" width="20" height="80" viewBox="0 0 20 80" aria-hidden="true">
        <line x1="13" y1="2" x2="7" y2="78" stroke="#e6e6e6" stroke-width="1.5"/>
      </svg>
      <div class="contact">
        <p>0061 555 0142</p>
        <p>info@copperlantern.com</p>
      </div>
    </section>
  </main>
</body>
</html>
```